詳細はzipファイルにまとめておりおますので、こちらからダウンロードしてください。

http://3.hakobuya.nu/0522-k83920fa17de462093b8e1c7f06a35d9

【デザインの参考サイト】
クライアント様からは、以下の参考サイトを挙げていただいております。
http://plumtivra.com/
https://sorvik4417.com/

ただし、上記サイトはおしゃれではあるものの、少しアピールが弱いようにも思います。
最終的な成果(査定依頼や、来店予約)に結びつきやすいような工夫があれば嬉しいです。

【継続発注について】
まずはトップページのみのデザインをお願い致します。
トップページのデザインが決まりましたら、下層ページのデザインもお願いする予定です。(1ページ1~2万円程度の予定)
下層ページは2~3ページほどの予定ですので、総額12万円ぐらいの予定です。

【スマホ対応について】
コーディング時に、レスポンシブ対応する予定ですので、スマホ対応しやすいデザインにしていただければ助かります。

【レイアウトの変更などについて】
基本的にはワイヤーに沿って作っていただければと思います。
ただし、「もっとこうしたほうが良いのでは?」「こんな形はどうか?」といったようなご提案があれば、別途ご相談ください。

必要な資料は上記のzipファイルの中に入れておりますので、そちらをご覧ください。
もし不明な点があれば遠慮なくご連絡くださいませ。
1ページ
シンプル 複雑
単色 カラフル
暗い 明るい
日常 高級
遊び心 厳粛
未来的 伝統的
女性的 男性的
黄・オレンジ系
• 高解像度JPG (.jpg)
• イラストレーター形式 (.ai)
納品は、IllustratorでもPhotoshopでもFireworksでも、どのファイルでもOKです。

また、納品の際には使っているフォントをお教えください。
(使用フォントはモリサワ、もしくはフリーフォントでお願いします)
たくさんのご応募ありがとうございました。
非常に悩んだのですが、お一人の方を選ばせていただきました。
選に漏れた方々につきましては、お手数おかけしたにも関わらず何もお返しできずに心苦しくもあるのですが、ご了承いただければ幸いです。
またこれに懲りず、今後ともよろしくお願いいたします。
ありがとうございました!

いいデザインをしていただいた方が数人おられて、非常に悩みました。
その中で一番こちらの意図を汲み取っていただき、バランスの取れたデザインをしていただいた、ということで、こちらの方にお願いすることにしました。

たくさんのご応募ありがとうございました。
ありがとうございました!

```html
<!DOCTYPE html>
<html lang="ja">
<head>
<meta charset="utf-8">
<title>タカミエ | 7階以上の高層階限定マンション買取サービス</title>
<link href="https://fonts.googleapis.com/css2?family=Noto+Sans+JP:wght@400;500;700;900&display=swap" rel="stylesheet">
<style>
:root{
  --orange:#f29a2e;
  --orange-deep:#e8851a;
  --orange-pale:#fde3c4;
  --ink:#3c3c3c;
  --gray:#8a8a8a;
  --line:#d8d8d8;
  --bg-soft:#f2f2f2;
  --dark:#4a4a4a;
  --white:#fff;
}
*{box-sizing:border-box;margin:0;padding:0}
html,body{width:1200px;height:4724px;overflow:hidden}
body{font-family:"Noto Sans JP",sans-serif;color:var(--ink);background:var(--white);position:relative}
.section{position:absolute;left:0;width:1200px}
.brand{font-weight:900;letter-spacing:4px;color:var(--orange);white-space:nowrap}

/* header */
.site-header{top:0;height:92px;background:rgba(255,255,255,.94);z-index:5;display:flex;align-items:center;padding:0 48px}
.site-header .brand{font-size:34px;margin-right:18px}
.site-header .tagline{font-size:13px;line-height:1.5;color:var(--ink);white-space:nowrap}
.global-nav{margin-left:auto;display:flex;gap:30px;font-size:15px}
.global-nav a{color:var(--ink);text-decoration:none}
.global-nav a.current{color:var(--orange)}

/* hero */
.hero{top:0;height:735px;overflow:hidden}
.hero-photo{position:absolute;inset:0;background:linear-gradient(115deg,#e9e3da 0%,#d6cec2 35%,#c9cfd6 60%,#aab6c2 100%)}
.hero-shapes{position:absolute;inset:0}
.hero-copy{position:absolute;left:690px;top:330px;text-align:left}
.hero-copy h1{font-size:50px;font-weight:500;line-height:1.45;color:#333;letter-spacing:2px}
.hero-copy .brand{font-size:28px;margin-top:12px;display:block}
.hero-dots{top:745px;height:20px;display:flex;justify-content:center;gap:22px}
.hero-dots span{width:16px;height:16px;border-radius:50%;background:#c9c9c9}
.hero-dots span.on{background:var(--orange)}

/* intro */
.intro{top:815px;text-align:center;font-size:18px;line-height:2.1}

/* about */
.about{top:990px;height:400px;background:var(--orange);color:var(--white);text-align:center}
.section-title-en{font-size:34px;font-weight:700;letter-spacing:3px;padding-top:26px;line-height:1.4}
.section-title-sub{font-size:16px;line-height:1.4}
.about-list{display:flex;justify-content:center;gap:90px;margin-top:20px}
.about-item{width:250px}
.about-icon{width:66px;height:66px;margin:0 auto 10px;display:block}
.about-item h3{font-size:16px;font-weight:700;line-height:1.5;margin-bottom:6px}
.about-item p{font-size:12px;line-height:1.7}
.btn-outline{display:inline-block;margin-top:18px;padding:10px 56px;border:2px solid var(--white);background:rgba(255,255,255,.15);color:var(--white);font-size:16px;text-decoration:none}

/* compare */
.compare{top:1390px;height:970px}
.compare h2{text-align:center;font-size:40px;font-weight:700;padding-top:30px}
.compare-diagram{position:absolute;left:0;top:110px;width:1200px;height:520px}
.diagram-fill{position:absolute;border-radius:4px}
.diagram-fill.left{left:110px;top:150px;width:440px;height:300px;background:linear-gradient(180deg,#ececec,#d9d9d9)}
.diagram-fill.right{left:720px;top:150px;width:260px;height:250px;background:linear-gradient(180deg,#fbe0bd,#f6c68a)}
.diagram-label{position:absolute;font-size:20px;color:var(--ink)}
.compare-points{position:absolute;top:670px;left:0;width:1200px;display:grid;grid-template-columns:470px 470px;column-gap:80px;row-gap:36px;padding-left:115px}
.point h3{font-size:20px;font-weight:700;display:flex;align-items:center;gap:10px;margin-bottom:8px}
.point h3::before{content:"";width:8px;height:28px;background:var(--ink)}
.point.plus h3{color:var(--orange)}
.point.plus h3::before{background:var(--orange)}
.point p{font-size:15px;line-height:1.7}
.point.plus p{color:var(--orange)}

/* faq */
.faq{top:2360px;height:840px;background:var(--orange)}
.faq h2{text-align:center;color:var(--white);font-size:40px;font-weight:700;padding-top:36px}
.faq-grid{display:grid;grid-template-columns:repeat(3,320px);gap:34px 40px;justify-content:center;margin-top:34px}
.faq-card{background:var(--white);height:320px;padding:22px 20px}
.faq-q,.faq-a{display:flex;gap:12px}
.faq-q{font-size:18px;font-weight:700;line-height:1.4;padding-bottom:16px;border-bottom:1px solid var(--line);margin-bottom:16px}
.faq-mark{flex:none;width:32px;height:32px;font-size:24px;font-weight:900;line-height:32px;text-align:center;color:var(--white);background:var(--orange)}
.faq-a .faq-mark{background:none;color:var(--orange)}
.faq-a p{font-size:13px;line-height:1.75}

/* results */
.results{top:3200px;height:1100px;text-align:center}
.results h2{font-size:40px;font-weight:700;padding-top:40px}
.results .lead{font-size:15px;margin-top:4px}
.result-card{position:absolute;left:130px;width:940px;height:390px;background:var(--bg-soft);border:1px solid var(--line);text-align:left}
.result-photo{position:absolute;left:30px;top:34px;width:220px;height:200px;background:linear-gradient(135deg,#c9c2b6,#9aa3ab)}
.btn-gray{position:absolute;display:block;text-align:center;background:#7a7a7a;color:var(--white);font-size:15px;text-decoration:none;box-shadow:0 3px 0 #555}
.result-card .btn-gray{left:50px;top:256px;width:180px;height:42px;line-height:42px}
.result-name{position:absolute;left:280px;top:40px;width:240px;font-size:19px;font-weight:700;line-height:1.5;padding-bottom:12px;border-bottom:2px solid var(--orange)}
.result-spec{position:absolute;left:280px;top:140px;font-size:16px;line-height:2.05}
.result-spec dt{display:inline-block;width:74px}
.result-spec dd{display:inline}
.result-note{position:absolute;left:560px;top:40px;width:330px;height:300px;background:var(--orange-pale);color:var(--orange-deep);padding:18px;font-size:15px;line-height:1.8}
.results .btn-more{left:460px;top:1010px;width:280px;height:50px;line-height:50px;font-size:16px}

/* cta */
.cta{top:4320px;height:140px;background:var(--bg-soft);display:flex;justify-content:center;align-items:center;gap:60px}
.cta a{position:relative;display:block;width:390px;height:76px;line-height:76px;background:var(--dark);color:var(--white);font-size:24px;font-weight:700;text-decoration:none;padding-left:60px}
.cta a::before{content:"";position:absolute;left:28px;top:30px;border:9px solid transparent;border-left:12px solid var(--orange)}
.to-top{position:absolute;right:40px;top:4270px;width:110px;height:52px;background:var(--orange);color:var(--white);font-size:14px;text-align:center;padding-top:22px;border-radius:55px 55px 0 0;text-decoration:none}

/* footer */
.site-footer{top:4460px;height:264px;background:var(--white);border-top:4px solid var(--orange)}
.footer-main{display:flex;padding:34px 60px 0;gap:34px}
.footer-brand{flex:none}
.footer-brand .row{display:flex;align-items:center;gap:14px}
.footer-brand .brand{font-size:32px}
.footer-brand .tagline{font-size:12px;line-height:1.5;white-space:nowrap}
.footer-brand address{font-style:normal;font-size:13px;line-height:1.7;margin-top:10px}
.footer-nav{flex:none;display:grid;grid-template-columns:repeat(4,auto);gap:6px 26px;font-size:14px;height:50px}
.footer-nav a{color:var(--ink);text-decoration:none;white-space:nowrap}
.footer-info{width:290px;font-size:12px;line-height:1.7;color:var(--gray);padding-left:20px;border-left:1px solid var(--line)}
.copyright{position:absolute;bottom:0;left:0;width:1200px;height:36px;line-height:36px;background:var(--orange);color:var(--white);font-size:12px;text-align:center}
</style>
</head>
<body>

<header class="section site-header">
  <span class="brand">タカミエ</span>
  <span class="tagline">7階以上の高層階限定<br>マンション買取サービス</span>
  <nav class="global-nav">
    <a class="current">タカミエとは</a><a>買取の流れ</a><a>買取実績</a><a>買取無料査定</a><a>ご来店予約</a>
  </nav>
</header>

<section class="section hero">
  <div class="hero-photo" role="img" aria-label="高層マンションの明るいリビングと窓からの街並み"></div>
  <svg class="hero-shapes" width="1200" height="735" viewBox="0 0 1200 735">
    <polygon points="0,560 300,735 0,735" fill="#f29a2e" opacity=".9"/>
    <polygon points="0,640 160,735 0,735" fill="#e8851a"/>
    <polygon points="1200,470 1200,735 760,735" fill="#f29a2e" opacity=".9"/>
    <polygon points="1200,600 1200,735 980,735" fill="#e8851a"/>
    <polygon points="640,290 1130,290 1090,510 600,510" fill="#ffffff" opacity=".85"/>
  </svg>
  <div class="hero-copy">
    <h1>7階以上のお部屋、<br>買い取ります。</h1>
    <span class="brand">タカミエ</span>
  </div>
</section>

<div class="section hero-dots"><span class="on"></span><span></span><span></span><span></span><span></span><span></span></div>

<section class="section intro">
  <p>「タカミエ」は、7階以上の高層階限定のマンション売買サービスです。</p>
  <p>見晴らしの良い高層階のマンションは、それだけでも価値をつけてくれる特別な価値を持っています。</p>
  <p>「タカミエ」は、その価値に見合った金額で、マンションを買い取らせていただきます。</p>
</section>

<section class="section about">
  <p class="section-title-en">ABOUT</p>
  <p class="section-title-sub"><b>タカミエ</b> について</p>
  <div class="about-list">
    <div class="about-item">
      <svg class="about-icon" viewBox="0 0 78 78"><circle cx="39" cy="39" r="36" fill="none" stroke="#fff" stroke-width="3"/><rect x="22" y="30" width="34" height="22" rx="3" fill="none" stroke="#fff" stroke-width="3"/><circle cx="39" cy="41" r="5" fill="#fff"/></svg>
      <h3>納得の金額をご提示します!<br>&nbsp;</h3>
      <p>高層階の価値を正しく評価し、<br>相場に見合った金額をご提示します。</p>
    </div>
    <div class="about-item">
      <svg class="about-icon" viewBox="0 0 78 78"><circle cx="39" cy="39" r="36" fill="none" stroke="#fff" stroke-width="3"/><rect x="26" y="20" width="26" height="38" rx="3" fill="none" stroke="#fff" stroke-width="3"/><path d="M32 30h14M32 38h14M32 46h8" stroke="#fff" stroke-width="3"/></svg>
      <h3>現金化もスピーディ<br>費用も現金化できます</h3>
      <p>ご契約から入金までが早く、<br>急なご事情にも対応いたします。</p>
    </div>
    <div class="about-item">
      <svg class="about-icon" viewBox="0 0 78 78"><circle cx="39" cy="39" r="36" fill="none" stroke="#fff" stroke-width="3"/><path d="M24 40l10 10 20-22" fill="none" stroke="#fff" stroke-width="4"/></svg>
      <h3>直接買取なので<br>仲介手数料もかかりません</h3>
      <p>当社が直接買い取るため、<br>仲介手数料は一切不要です。</p>
    </div>
  </div>
  <a class="btn-outline">詳しくはこちら</a>
</section>

<section class="section compare">
  <h2>一括見積もりサイトとの違い</h2>
  <div class="compare-diagram">
    <svg width="1200" height="140" viewBox="0 0 1200 140" style="position:absolute;left:0;top:0">
      <text x="330" y="20" font-size="22" text-anchor="middle" fill="#3c3c3c" font-family="Noto Sans JP, sans-serif">一括見積もりサイトの場合</text>
      <line x1="170" y1="38" x2="490" y2="38" stroke="#3c3c3c"/>
      <text x="850" y="20" font-size="22" text-anchor="middle" fill="#f29a2e" font-weight="700" font-family="Noto Sans JP, sans-serif">タカミエの場合</text>
      <line x1="720" y1="38" x2="980" y2="38" stroke="#f29a2e" stroke-width="2"/>
      <rect x="160" y="70" width="340" height="54" fill="#b3b3b3"/>
      <text x="330" y="104" font-size="18" fill="#fff" text-anchor="middle" font-family="Noto Sans JP, sans-serif">一括見積もりサイト</text>
      <path d="M535 97 h130 M555 82 l-20 15 20 15 M645 82 l20 15 -20 15" stroke="#f29a2e" stroke-width="6" fill="none"/>
      <rect x="700" y="70" width="300" height="54" fill="#f29a2e"/>
      <text x="850" y="105" font-size="22" fill="#fff" text-anchor="middle" font-weight="900" font-family="Noto Sans JP, sans-serif">タカミエ</text>
    </svg>
    <div class="diagram-fill left" role="img" aria-label="一括見積もりサイトから多数の不動産業者へ情報が渡り、各社からお客様へ営業が届く流れの図"></div>
    <span class="diagram-label" style="left:565px;top:245px">不動産業者</span>
    <span class="diagram-label" style="left:565px;top:410px">お客様</span>
    <div class="diagram-fill right" role="img" aria-label="高層マンションから直接お客様へ買取のご提案が届く流れの図"></div>
    <span class="diagram-label" style="left:1000px;top:260px">お客様</span>
  </div>
  <div class="compare-points">
    <div class="point"><h3>個人情報が多くの会社に行き渡る</h3><p>個人情報が多くの会社に行き渡ってしまうので、<br>電話・DMなどの営業が激しく、収集がつかなくなります</p></div>
    <div class="point plus"><h3>最初から相場の価格を提示</h3><p>最初から相場に近い価格を提示しますので、<br>時間をかけずに安心してお取引いただけます</p></div>
    <div class="point"><h3>最初の見積もりより安く売られる</h3><p>最初は相場より高く見積もりますが、結局その<br>見積もりで売れずに、値下げして売ることになります</p></div>
    <div class="point plus"><h3>仲介業者もありません</h3><p>仲介業者を通さず直接買い取るので、<br>仲介手数料は一切かかりません</p></div>
  </div>
</section>

<section class="section faq">
  <h2>よくある質問</h2>
  <div class="faq-grid">
    <div class="faq-card"><div class="faq-q"><span class="faq-mark">Q</span>質問が入ります。質問が入ります。</div><div class="faq-a"><span class="faq-mark">A</span><p>回答テキストが入ります。回答テキストが入ります。回答テキストが入ります。回答テキストが入ります。回答テキストが入ります。回答テキストが入ります。回答テキストが入ります。回答テキストが入ります。</p></div></div>
    <div class="faq-card"><div class="faq-q"><span class="faq-mark">Q</span>質問が入ります。質問が入ります。</div><div class="faq-a"><span class="faq-mark">A</span><p>回答テキストが入ります。回答テキストが入ります。回答テキストが入ります。回答テキストが入ります。回答テキストが入ります。回答テキストが入ります。回答テキストが入ります。回答テキストが入ります。</p></div></div>
    <div class="faq-card"><div class="faq-q"><span class="faq-mark">Q</span>質問が入ります。質問が入ります。</div><div class="faq-a"><span class="faq-mark">A</span><p>回答テキストが入ります。回答テキストが入ります。回答テキストが入ります。回答テキストが入ります。回答テキストが入ります。回答テキストが入ります。回答テキストが入ります。回答テキストが入ります。</p></div></div>
    <div class="faq-card"><div class="faq-q"><span class="faq-mark">Q</span>質問が入ります。質問が入ります。</div><div class="faq-a"><span class="faq-mark">A</span><p>回答テキストが入ります。回答テキストが入ります。回答テキストが入ります。回答テキストが入ります。回答テキストが入ります。回答テキストが入ります。回答テキストが入ります。回答テキストが入ります。</p></div></div>
    <div class="faq-card"><div class="faq-q"><span class="faq-mark">Q</span>質問が入ります。質問が入ります。</div><div class="faq-a"><span class="faq-mark">A</span><p>回答テキストが入ります。回答テキストが入ります。回答テキストが入ります。回答テキストが入ります。回答テキストが入ります。回答テキストが入ります。回答テキストが入ります。回答テキストが入ります。</p></div></div>
    <div class="faq-card"><div class="faq-q"><span class="faq-mark">Q</span>質問が入ります。質問が入ります。</div><div class="faq-a"><span class="faq-mark">A</span><p>回答テキストが入ります。回答テキストが入ります。回答テキストが入ります。回答テキストが入ります。回答テキストが入ります。回答テキストが入ります。回答テキストが入ります。回答テキストが入ります。</p></div></div>
  </div>
</section>

<section class="section results">
  <h2>買取実績</h2>
  <p class="lead">関西一円対応いたします。</p>
  <article class="result-card" style="top:170px">
    <div class="result-photo" role="img" aria-label="買取物件の室内写真"></div>
    <a class="btn-gray">詳しくはこちら</a>
    <h3 class="result-name">物件名が入ります。物件名が入ります。</h3>
    <dl class="result-spec"><dt>■階数</dt><dd>:10階</dd><br><dt>■間取り</dt><dd>:2LDK</dd><br><dt>■価格</dt><dd>:3500万円</dd><br><dt>■地域</dt><dd>:大阪市内</dd></dl>
    <p class="result-note">テキストが入ります。テキストが入ります。テキストが入ります。テキストが入ります。テキストが入ります。テキストが入ります。テキストが入ります。テキストが入ります。テキストが入ります。</p>
  </article>
  <article class="result-card" style="top:590px">
    <div class="result-photo" role="img" aria-label="買取物件の室内写真"></div>
    <a class="btn-gray">詳しくはこちら</a>
    <h3 class="result-name">物件名が入ります。物件名が入ります。</h3>
    <dl class="result-spec"><dt>■階数</dt><dd>:10階</dd><br><dt>■間取り</dt><dd>:2LDK</dd><br><dt>■価格</dt><dd>:3500万円</dd><br><dt>■地域</dt><dd>:大阪市内</dd></dl>
    <p class="result-note">テキストが入ります。テキストが入ります。テキストが入ります。テキストが入ります。テキストが入ります。テキストが入ります。テキストが入ります。テキストが入ります。テキストが入ります。</p>
  </article>
  <a class="btn-gray btn-more">買取実績をもっとみる</a>
</section>

<a class="to-top">トップへ</a>
<section class="section cta">
  <a>買取無料査定はこちら</a>
  <a>ご来店予約はこちら</a>
</section>

<footer class="section site-footer">
  <div class="footer-main">
    <div class="footer-brand">
      <div class="row"><span class="brand">タカミエ</span><span class="tagline">7階以上の高層階限定<br>マンション買取サービス</span></div>
      <address>運営：株式会社ソラノハウス<br>〒530-0047<br>大阪府大阪市北区梅園町3-8-2<br>TEL:06-4521-7380</address>
    </div>
    <nav class="footer-nav">
      <a>タカミエについて</a><a>買取の流れ</a><a>買取実績</a><a>買取無料査定</a>
      <a>ご来店予約</a><a>お問い合わせ</a><a>会社概要</a><a>プライバシーポリシー</a>
    </nav>
    <p class="footer-info">「タカミエ」は、不動産業の株式会社ソラノハウスが運営しているサービスです。お気軽にご相談ください。</p>
  </div>
  <p class="copyright">Copyright © 2017 Sorano House Co.Ltd All Rights Reserved.</p>
</footer>

</body>
</html>
```